CD/Album cover design - Ember & Tide

Hi, I need an album cover designed. The name of the album is called 'Ember and Tide' Not 100% sure of the concept, but using colored lines, Geometrical shapes etc, angles and maybe a circle or triangle in the middle. A cross between, Velvet Harbor ,Hollow rim of the sea (But dont make it look like this old look album) , 80s retro synthwave album covers, perhaps with neon color lines but not all of it etc. Have it modern looking . My name on cover and album name. Back, songs etc and info details. The style of the music is EDM meets guitar. Trap, house music and guitar as the main theme instrument, with sythns. Keep it relatively simple looking, and maybe have the background white,, but with the color designs, wording etc colors. or if you feel it would look better another way, just use your own judgement and creativity. Ve attached a couple of Pics. The Velvet Harbor pic , more of concept. The retro one... I like the design in the middle but not wording at the top. The QX rise one, I like how the wording is in the middle of circle. So a combination of these, with geometrical lines, colors, etc. I am also open to a completely new idea that you think would look awesome. The album is really combining Guitar with House/Tap EDM music, and the concept Ember and Tide - The beginning and end (Of everything) Thanks
EDM , Guitarists
Music, EDM, Guitar Instrumental

```html
<!DOCTYPE html>
<html lang="en">
<head>
<meta charset="utf-8">
<title>Ember and Tide – Album Cover</title>
<link rel="stylesheet" href="https://fonts.googleapis.com/css2?family=Russo+One&family=Kaushan+Script&display=swap">
<style>
  :root {
    --paper: #ffffff;
    --ink: #000000;
    --neon-pink: #ff4fb8;
    --neon-red: #ff2a5f;
    --neon-violet: #9a6bff;
    --neon-green: #7dff6a;
    --neon-cyan: #6ff3ff;
    --title-lilac: #d7b3ea;
    --title-sky: #b9d6ff;
    --title-pink: #e6a9d6;
  }
  html, body {
    margin: 0;
    padding: 0;
    width: 1200px;
    height: 1200px;
    overflow: hidden;
    background: var(--paper);
  }
  .cover {
    position: relative;
    width: 1200px;
    height: 1200px;
    background: var(--paper);
    overflow: hidden;
  }
  .layer {
    position: absolute;
    inset: 0;
  }
  .emblem-artwork {
    position: absolute;
    left: 326px;
    top: 330px;
    width: 551px;
    height: 530px;
    border-radius: 40px;
    background: radial-gradient(ellipse at 50% 58%,
      #0a0610 0%,
      #1a0b24 38%,
      rgba(154, 107, 255, 0.85) 62%,
      rgba(255, 79, 184, 0.7) 78%,
      rgba(255, 79, 184, 0) 100%);
  }
  .artist-name {
    font-family: "Russo One", sans-serif;
  }
  .title-word {
    font-family: "Russo One", sans-serif;
  }
  .title-joiner {
    font-family: "Kaushan Script", cursive;
  }
</style>
</head>
<body>
<main class="cover">

  <svg class="layer light-streak" width="1200" height="1200" viewBox="0 0 1200 1200" aria-hidden="true">
    <defs>
      <filter id="glow-soft" x="-50%" y="-50%" width="200%" height="200%">
        <feGaussianBlur stdDeviation="22"/>
      </filter>
      <filter id="glow-line" x="-20%" y="-20%" width="140%" height="140%">
        <feGaussianBlur stdDeviation="4" result="blur"/>
        <feMerge><feMergeNode in="blur"/><feMergeNode in="SourceGraphic"/></feMerge>
      </filter>
      <linearGradient id="streak-colour" x1="0" y1="900" x2="1200" y2="330" gradientUnits="userSpaceOnUse">
        <stop offset="0" stop-color="var(--neon-green)" stop-opacity="0.4"/>
        <stop offset="0.2" stop-color="var(--neon-pink)"/>
        <stop offset="0.6" stop-color="#c35cff"/>
        <stop offset="0.85" stop-color="var(--neon-pink)"/>
        <stop offset="1" stop-color="var(--neon-cyan)"/>
      </linearGradient>
    </defs>
    <path d="M0 906 C90 880 170 870 212 800 C240 770 290 780 330 775 M790 600 C820 570 840 550 870 520 C900 480 960 430 1020 415 C1070 400 1110 385 1200 326"
          fill="none" stroke="url(#streak-colour)" stroke-width="70" opacity="0.5" filter="url(#glow-soft)"/>
    <path d="M0 906 C90 880 170 870 212 800 C240 770 290 780 330 775 M790 600 C820 570 840 550 870 520 C900 480 960 430 1020 415 C1070 400 1110 385 1200 326"
          fill="none" stroke="url(#streak-colour)" stroke-width="5" filter="url(#glow-line)"/>
    <path d="M0 906 C90 880 170 870 212 800 C240 770 290 780 330 775 M790 600 C820 570 840 550 870 520 C900 480 960 430 1020 415 C1070 400 1110 385 1200 326"
          fill="none" stroke="#ffffff" stroke-width="1.5" opacity="0.9"/>
  </svg>

  <div class="emblem-artwork" role="img" aria-label="Neon emblem: black triangle with glowing pink, yellow, green and violet nested triangle outlines, paint splatter and sparkles"></div>

  <svg class="layer" width="1200" height="1200" viewBox="0 0 1200 1200" aria-labelledby="album-title">
    <title id="album-title">Ember and Tide</title>
    <defs>
      <linearGradient id="title-fill" x1="0" y1="0" x2="1" y2="1">
        <stop offset="0" stop-color="var(--title-lilac)"/>
        <stop offset="0.5" stop-color="var(--title-sky)"/>
        <stop offset="1" stop-color="var(--title-pink)"/>
      </linearGradient>
    </defs>

    <text class="artist-name" transform="translate(68 360) rotate(-90)" font-size="34"
          textLength="296" lengthAdjust="spacingAndGlyphs" fill="var(--ink)">ARTIST NAME</text>

    <g class="album-title">
      <text class="title-word" x="302" y="624" font-size="122" textLength="342" lengthAdjust="spacingAndGlyphs"
            fill="url(#title-fill)" stroke="#ffffff" stroke-width="10" stroke-linejoin="round" paint-order="stroke">EMBER</text>
      <text class="title-word" x="302" y="624" font-size="122" textLength="342" lengthAdjust="spacingAndGlyphs"
            fill="url(#title-fill)" stroke="var(--ink)" stroke-width="4" stroke-linejoin="round" paint-order="stroke">EMBER</text>

      <text class="title-word" x="582" y="730" font-size="128" textLength="366" lengthAdjust="spacingAndGlyphs"
            fill="url(#title-fill)" stroke="#ffffff" stroke-width="10" stroke-linejoin="round" paint-order="stroke">TIDE</text>
      <text class="title-word" x="582" y="730" font-size="128" textLength="366" lengthAdjust="spacingAndGlyphs"
            fill="url(#title-fill)" stroke="var(--ink)" stroke-width="4" stroke-linejoin="round" paint-order="stroke">TIDE</text>

      <text class="title-joiner" x="584" y="662" font-size="56" fill="#ffffff"
            stroke="var(--ink)" stroke-width="3" paint-order="stroke" transform="rotate(-12 620 645)">and</text>
    </g>
  </svg>
</main>
</body>
</html>
```